FinTech company looking to revamp and expand client-facing interface for our financial models

Halvern Ledgerworks currently has a very simple website that allows clients to interact with our financial models. We are looking to completely redesign the current site and add several extra pages to provide extra functionality. We want the design to have a modern, slick feel, that will work on both a desktop or a tablet. It should be straightforward for clients to move between different pages at any time, and clear from the layout how to interact with the more advanced features. We have included screenshots of existing pages in the attached design brief, as well as sketches of the functionality required by the new pages, but can't provide a direct link to the current site.
Target Market(s)
Professional investors that will be paying to access the interface
Industry/Entity Type
Finance
Number of Pages Required
4 page
Colors
Designer to choose colors to be used in the design.
Look and feel
Each slider illustrates characteristics of the customer's brand and the style your logo design should communicate.

```html
<!DOCTYPE html>
<html lang="en">
<head>
<meta charset="utf-8">
<title>Halvern Ledgerworks – Factors</title>
<link rel="stylesheet" href="https://fonts.googleapis.com/css2?family=Open+Sans:wght@400;600;700&display=swap">
<style>
  :root {
    --ink: #231f20;
    --gold: #fdc51e;
    --gold-text: #f9c21c;
    --dark-chip: #1a1718;
  }
  * { box-sizing: border-box; margin: 0; padding: 0; }
  html, body { width: 1200px; height: 1124px; overflow: hidden; }
  body {
    position: relative;
    background: var(--ink);
    font-family: "Open Sans", sans-serif;
    color: var(--gold-text);
    letter-spacing: 2px;
  }
  .abs { position: absolute; }
  .rule { position: absolute; left: 2px; right: 2px; height: 3px; background: var(--gold); }

  .tabs { top: 118px; left: 128px; display: flex; gap: 0; font-size: 19px; font-weight: 600; }
  .tabs span { padding: 0 13px; line-height: 28px; }
  .tabs .first { padding-left: 0; margin-right: 12px; }
  .tabs .active { background: var(--dark-chip); }

  .brand { top: 108px; left: 498px; width: 200px; text-align: center; font-size: 21px; font-weight: 700; line-height: 24px; letter-spacing: 1px; }
  .brand small { display: block; font-size: 21px; }

  .menu { top: 123px; left: 704px; display: flex; align-items: center; font-size: 12.5px; font-weight: 600; }
  .menu .item { display: flex; align-items: center; gap: 7px; margin-right: 26px; }
  .menu .item:last-child { margin-left: 18px; }
  .menu svg { width: 16px; height: 16px; fill: var(--gold); }

  .thresholds { top: 320px; left: 136px; }
  .thr { display: flex; align-items: center; height: 33px; font-size: 19px; }
  .thr:nth-child(3) { margin-top: 3px; }
  .thr .stat { width: 90px; font-weight: 600; }
  .thr .lbl { width: 113px; font-weight: 700; }
  .thr .box { width: 138px; height: 19px; border: 1.5px solid var(--gold); font-size: 11px; font-weight: 700; line-height: 16px; padding-left: 8px; letter-spacing: 0.5px; }

  .head, .row { position: absolute; left: 0; width: 1200px; }
  .head { top: 448px; font-size: 16px; font-weight: 600; }
  .cell { position: absolute; }
  .c-factor { left: 145px; }
  .c-id { left: 315px; }
  .c-sector { left: 444px; }
  .num { text-align: center; width: 80px; }
  .s1 { left: 597px; } .s2 { left: 696px; } .s3 { left: 787px; } .s4 { left: 876px; } .s5 { left: 975px; }
  .head .c-factor { left: 145px; }
  .head .c-id { font-size: 19px; }
  .head .c-id svg { width: 12px; height: 8px; fill: var(--gold); margin-left: 6px; vertical-align: middle; }
  .head .c-sector { left: 465px; }
  .head-rule { position: absolute; top: 487px; left: 106px; width: 989px; height: 3px; background: var(--gold); }

  .row { font-size: 19px; font-weight: 600; line-height: 22px; }
  .row .c-factor { left: 128px; }
  .row .c-id { left: 307px; }

  .footer { position: absolute; left: 0; top: 913px; width: 1200px; height: 211px; background: var(--gold); color: var(--ink); }
  .f-brand { position: absolute; left: 140px; top: 70px; width: 180px; font-size: 21px; font-weight: 700; line-height: 25px; letter-spacing: 1px; }
  .contact { position: absolute; left: 371px; top: 26px; font-size: 15px; line-height: 20.5px; font-weight: 600; }
  .contact h3, .follow h3 { font-size: 19px; font-weight: 700; letter-spacing: 3px; margin-bottom: 2px; }
  .contact .indent { padding-left: 47px; }
  .divider { position: absolute; left: 689px; top: 24px; width: 1px; height: 120px; background: var(--ink); }
  .follow { position: absolute; left: 715px; top: 26px; }
  .socials { display: flex; gap: 25px; margin-top: 6px; }
  .socials span { width: 27px; height: 27px; background: var(--ink); display: block; }
  .news { display: flex; align-items: center; margin-top: 14px; }
  .news .label { font-size: 13px; font-weight: 600; border-top: 1px solid var(--ink); border-bottom: 1px solid var(--ink); padding: 1px 2px; line-height: 22px; margin-right: 9px; }
  .news .field { width: 202px; height: 21px; background: var(--ink); color: var(--gold); font-size: 13px; font-weight: 600; padding-left: 14px; line-height: 21px; margin-top: -4px; }
</style>
</head>
<body>
  <div class="rule" style="top:34px"></div>
  <div class="rule" style="top:41px"></div>

  <nav class="tabs abs">
    <span class="first">Factors</span>
    <span class="active">250D</span>
    <span>83D</span>
    <span>42D</span>
  </nav>

  <div class="brand abs">Halvern<small>Ledgerworks</small></div>

  <nav class="menu abs">
    <div class="item"><svg viewBox="0 0 16 16"><path d="M8 1 0 8h2v7h4v-5h4v5h4V8h2z"/></svg>MODELS</div>
    <div class="item"><svg viewBox="0 0 16 16"><path d="M8 0l1.5 2.5 2.8-.8.3 2.9 2.8 1-1.4 2.4 1.4 2.4-2.8 1-.3 2.9-2.8-.8L8 16l-1.5-2.5-2.8.8-.3-2.9-2.8-1L2 8 .6 5.6l2.8-1 .3-2.9 2.8.8z M8 5a3 3 0 1 0 0 6 3 3 0 0 0 0-6z" fill-rule="evenodd"/></svg>SENTIVITITES</div>
    <div class="item"><svg viewBox="0 0 16 16"><path d="M8 0l2.4 5 5.6.6-4.2 3.8 1.2 5.6L8 12.2 3 15l1.2-5.6L0 5.6 5.6 5z"/></svg>FAVOURITES</div>
  </nav>

  <div class="rule" style="top:219px"></div>
  <div class="rule" style="top:226px"></div>

  <section class="thresholds abs">
    <div class="thr"><span class="stat">Stat 1</span><span class="lbl">Treshold:</span><span class="box">-10</span></div>
    <div class="thr"><span class="stat">Stat 2</span><span class="lbl">Treshold:</span><span class="box">-10</span></div>
    <div class="thr"><span class="stat">Stat 3</span><span class="lbl">Treshold:</span><span class="box">-10</span></div>
  </section>

  <div class="head">
    <span class="cell c-factor">Factors</span>
    <span class="cell c-id">ID<svg viewBox="0 0 12 8"><path d="M0 0h12L6 8z"/></svg></span>
    <span class="cell c-sector">Sector</span>
    <span class="cell num s1">Stat 1</span>
    <span class="cell num s2">Stat 2</span>
    <span class="cell num s3">Stat 3</span>
    <span class="cell num s4">Stat 4</span>
    <span class="cell num s5">Stat 5</span>
  </div>
  <div class="head-rule"></div>

  <div class="row" style="top:522px">
    <span class="cell c-factor">Factor 1</span><span class="cell c-id">Model 1</span>
    <span class="cell c-sector">Materials</span>
    <span class="cell num s1">-1.4</span><span class="cell num s2">0.1</span><span class="cell num s3">-3.1</span><span class="cell num s4">0.7</span><span class="cell num s5">0.9</span>
  </div>
  <div class="row" style="top:584px">
    <span class="cell c-factor">Factor 2</span><span class="cell c-id">Model 2</span>
    <span class="cell c-sector">Industrails</span>
    <span class="cell num s1" style="top:2px">2.8</span><span class="cell num s2">0.1</span><span class="cell num s3">6.1</span><span class="cell num s4">100</span><span class="cell num s5">0.9</span>
  </div>
  <div class="row" style="top:648px">
    <span class="cell c-factor">Factor 3</span><span class="cell c-id" style="top:8px">Model 3</span>
    <span class="cell c-sector">Consumer<br>Discretionary</span>
    <span class="cell num s1">-3.7</span><span class="cell num s2">2.7</span><span class="cell num s3">-7.2</span><span class="cell num s4">100</span><span class="cell num s5">0.9</span>
  </div>
  <div class="row" style="top:719px">
    <span class="cell c-factor">Factor 4</span><span class="cell c-id" style="top:-2px">Model 4</span>
    <span class="cell c-sector">Information<br>Technology</span>
    <span class="cell num s1" style="left:603px">2.8</span><span class="cell num s2" style="top:-2px">0.2</span><span class="cell num s3" style="top:-2px">2.7</span><span class="cell num s4" style="top:-2px">0.5</span><span class="cell num s5" style="top:-2px">-0.5</span>
  </div>
  <div class="row" style="top:790px">
    <span class="cell c-factor">Factor 5</span><span class="cell c-id" style="top:-2px">Model 5</span>
    <span class="cell c-sector">Information<br>Technology</span>
    <span class="cell num s1">0.8</span><span class="cell num s2">0.3</span><span class="cell num s3">2.5</span><span class="cell num s4">0.5</span><span class="cell num s5">-0.5</span>
  </div>

  <footer class="footer">
    <div class="f-brand">Halvern<br>Ledgerworks</div>
    <div class="contact">
      <h3>Contact</h3>
      <p>Phone: 415 555 0142</p>
      <p>Email: info@halvern.example</p>
      <p>Add: 88 Quillon Ave. #204</p>
      <p class="indent">Brightmoor, Ca 90000</p>
    </div>
    <div class="divider"></div>
    <div class="follow">
      <h3>Follow</h3>
      <div class="socials"><span></span><span></span><span></span><span></span></div>
      <div class="news"><span class="label">News Letters</span><span class="field">Enter Your Email</span></div>
    </div>
  </footer>
</body>
</html>
```